Business card design needed

would like the title calloway estate works to itself be a logo which would also be suitable to use on my van signwriting so needs to be bold and stand out (easily read from a distance)
Target Market(s)
real estate agents, property owners/investors,insurance assessors,
Industry/Entity Type
Business
Contact Information for Business Card
calloway estate works
for all your property maintenance and repair needs
-domestic and commercial -rental properties
-insurance repairs -project managment
fully insured/white card
experieced and reliable
ph. ned calloway 0418526093 email nedster4731@webhollow.net.au
on reverse side of card i would like a list of sevices available
plaster repairs
painting
welding reairs and fabrication
concreting
fencing
minor renovations
pressure cleaning
graffitti removal
rubbish removal
fire restorations
floods
and more no job too big or small
Logo Text
Logo styles of interest
Wordmark Logo

```html
<!DOCTYPE html>
<html lang="en">
<head>
<meta charset="utf-8">
<title>Calloway Estate Works – Business Card</title>
<link rel="stylesheet" href="https://fonts.googleapis.com/css2?family=Montserrat:wght@600;700&family=Questrial&family=Arimo:wght@700&display=swap">
<style>
  :root {
    --navy: #0c2a6e;
    --ink: #0a0a0a;
    --white: #ffffff;
    --band-deep: #0a2a8a;
    --band-mid: #1747c2;
    --band-light: #3f7cf0;
    --ghost: rgba(255, 255, 255, 0.09);
  }
  * { margin: 0; padding: 0; box-sizing: border-box; }
  html, body {
    width: 1200px;
    height: 693px;
    overflow: hidden;
    background: var(--white);
  }
  .card {
    position: relative;
    width: 1200px;
    height: 693px;
    background: var(--white);
    overflow: hidden;
  }
  .wordmark {
    position: absolute;
    left: 44px;
    top: 152px;
    color: var(--navy);
    font-family: "Montserrat", sans-serif;
    font-weight: 700;
    line-height: 1;
  }
  .wordmark__primary {
    display: block;
    font-size: 110px;
    letter-spacing: -1px;
  }
  .wordmark__secondary {
    display: block;
    margin-top: 10px;
    font-size: 60px;
    letter-spacing: 0.5px;
  }
  .contact {
    position: absolute;
    right: 50px;
    top: 126px;
    text-align: right;
  }
  .contact__name {
    font-family: "Montserrat", sans-serif;
    font-weight: 700;
    font-size: 54px;
    color: var(--navy);
    line-height: 1;
  }
  .contact__phone {
    margin-top: 22px;
    font-family: "Arimo", sans-serif;
    font-weight: 700;
    font-size: 68px;
    color: var(--ink);
    line-height: 1;
    letter-spacing: 1px;
  }
  .contact__email {
    margin-top: 20px;
    font-family: "Questrial", sans-serif;
    font-size: 28px;
    color: var(--ink);
    line-height: 1;
  }
  .services-band {
    position: absolute;
    left: 0;
    top: 347px;
    width: 1200px;
    height: 346px;
    background:
      radial-gradient(ellipse 55% 70% at 22% 25%, var(--band-light) 0%, rgba(63,124,240,0) 70%),
      linear-gradient(180deg, var(--band-mid) 0%, var(--band-deep) 100%);
    overflow: hidden;
  }
  .services-band__ghost {
    position: absolute;
    left: 40px;
    top: 210px;
    font-family: "Montserrat", sans-serif;
    font-weight: 700;
    font-size: 170px;
    color: var(--ghost);
    white-space: nowrap;
    transform: rotate(-12deg);
    transform-origin: left top;
    line-height: 1;
  }
  .services {
    position: absolute;
    left: 0;
    top: 64px;
    width: 100%;
    text-align: center;
    color: var(--white);
  }
  .services__lead {
    font-family: "Montserrat", sans-serif;
    font-weight: 700;
    font-size: 32px;
    line-height: 1;
  }
  .services__row {
    font-family: "Questrial", sans-serif;
    font-size: 37px;
    line-height: 1;
    margin-top: 20px;
  }
  .services__sep { margin: 0 22px; }
</style>
</head>
<body>
  <div class="card">
    <div class="wordmark" aria-label="Calloway Estate Works">
      <span class="wordmark__primary">Calloway</span>
      <span class="wordmark__secondary">Estate Works</span>
    </div>

    <div class="contact">
      <div class="contact__name">Ned Calloway</div>
      <div class="contact__phone">0418 526 093</div>
      <div class="contact__email">nedster4731@webhollow.net.au</div>
    </div>

    <section class="services-band">
      <div class="services-band__ghost" aria-hidden="true">Calloway Estate Works</div>
      <div class="services">
        <p class="services__lead">For all your property maintenance and repair needs:</p>
        <p class="services__row">Domestic and Commercial<span class="services__sep">|</span>Rental Properties</p>
        <p class="services__row">Insurance Repairs<span class="services__sep">|</span>Project Management</p>
        <p class="services__row">Fully Insured/White Card<span class="services__sep">|</span>Experienced &amp; Reliable</p>
      </div>
    </section>
  </div>
</body>
</html>
```